Comedy Hypnotist Morlan T Show Poster

I need a poster that can send to clubs that book my show for them in turn to use to promote me/my show at their club. The poster needs to be fun and attractive, and to have a blank space at the bottom where the club(s) can add the details particular to their show. [You'll have seen these posters everywhere for bands etc.]

I'm not fussy about whether or not you use the colours from my website or any of my photos. But do capture at least the essence of the logo somewhere.

I am not like other hypnotists - I want to convey an image of amazing hilarious fun, that everyone can enjoy. [NO Watches, NO Chickens and NO Spirals]. My show is hilarious and clean.

I come across as a little geeky, and very professional. Not sleazy or creepy. But fun, professional and easy to deal with. The show is loud, buzzy and amazing. People literally laugh until they cry. I use great lighting and amazing sound to make it a real event. I aim to entertain everyone. I am never mean and don't pick on or exploit people. (Check the website for video links and more images as well as the crap posters I use now) www.morlant-shows.example.

Somehow I want people who see my poster to go - that looks like fun! Lets check it out. I would so totally go to that.

It's worth looking at the website and the youtube vid to get a feel for what I do. The pictures you'll see are colourful and active.

My logo is newish - I like it because it is simple, professional and elegant - and different from other hypnotists. In a way that is my main marketing angle - I am different from other hypnotists.

Posters should be international paper A3 size.

Target Market(s)

entertainment, comedy, hypnotist

Industry/Entity Type

Entertainment Industry

Font styles to use
Sans Serif

Requirements
Must have
• Space at the bottom (white space) for people to write the details of their event on.
• "www.morlant-shows.example" in case they want to look me up.
• "Comedy Hypnotist"
• "Morlan T"
Nice to have
• Simple and clean designs. You don't have to use the logo but if you reference it somehow that would be better so they tie together. I have included some studio photos of myself but these are not required for the poster. You can choose not to include any picture - they are there for if you want them for your design idea.
Should not have
• Spirals, Watches, Chickens

```html
<!DOCTYPE html>
<html lang="en">
<head>
<meta charset="utf-8">
<title>Morlan T – Comedy Hypnotist Poster</title>
<link href="https://fonts.googleapis.com/css2?family=Anton&family=Roboto+Condensed:wght@800&display=swap" rel="stylesheet">
<style>
  :root {
    --navy-top: #02081f;
    --navy-mid: #06205e;
    --stage-blue: #1f6fe0;
    --glow-blue: #4fa6ff;
    --headline-yellow: #ffd21f;
    --headline-shadow: #b88a00;
    --ink: #111111;
    --paper: #ffffff;
  }
  * { margin: 0; padding: 0; box-sizing: border-box; }
  html, body { width: 800px; height: 1200px; overflow: hidden; background: var(--paper); }
  .poster {
    position: relative;
    width: 800px;
    height: 1200px;
    overflow: hidden;
    background:
      repeating-linear-gradient(90deg, rgba(255,255,255,0) 0 38px, rgba(120,190,255,0.10) 38px 46px, rgba(255,255,255,0) 46px 80px),
      linear-gradient(180deg, var(--navy-top) 0%, var(--navy-mid) 35%, var(--stage-blue) 62%, var(--glow-blue) 75%);
  }
  .web-address {
    position: absolute;
    top: 30px;
    right: 44px;
    font-family: "Roboto Condensed", "Arial Narrow", sans-serif;
    font-weight: 800;
    font-size: 25px;
    color: var(--headline-yellow);
    letter-spacing: 0.3px;
  }
  .performer-photo {
    position: absolute;
    left: 10px;
    top: 135px;
    width: 380px;
    height: 740px;
    background: linear-gradient(180deg, rgba(200,185,175,0.55) 0%, rgba(225,230,236,0.45) 32%, rgba(30,30,36,0.7) 55%, rgba(15,15,20,0.75) 100%);
    border-radius: 140px 140px 30px 30px;
  }
  .stage-badge {
    position: absolute;
    left: 364px;
    top: 172px;
    width: 382px;
    height: 382px;
    border-radius: 50%;
    border: 4px solid var(--headline-yellow);
    background: radial-gradient(circle at 50% 15%, #d9ecff 0%, #4f8fe0 35%, #1c4aa8 70%, #0f2f7a 100%);
  }
  .headline {
    position: absolute;
    left: 340px;
    top: 360px;
    width: 440px;
    font-family: "Anton", "Impact", sans-serif;
    color: var(--headline-yellow);
    text-transform: uppercase;
    line-height: 0.95;
    transform: rotate(-6deg);
    text-shadow: 4px 4px 0 var(--headline-shadow);
  }
  .headline .line-one { display: block; font-size: 104px; letter-spacing: 1px; }
  .headline .line-two { display: block; font-size: 66px; padding-left: 100px; letter-spacing: 1px; }
  .details-panel {
    position: absolute;
    left: 0;
    bottom: 0;
    width: 800px;
    height: 380px;
  }
  .act-name {
    position: absolute;
    left: 0;
    top: 872px;
    width: 800px;
    text-align: center;
    font-family: "Anton", "Impact", sans-serif;
    font-size: 176px;
    line-height: 1;
    color: var(--ink);
    text-transform: uppercase;
    letter-spacing: 4px;
  }
</style>
</head>
<body>
  <main class="poster">
    <div class="web-address">www.morlant-shows.example</div>

    <div class="stage-badge" role="img" aria-label="Stage lights shining on a vintage microphone in front of a brick wall"></div>

    <div class="performer-photo" role="img" aria-label="Studio photo of the smiling hypnotist in glasses, white shirt and black waistcoat, holding a G-rated card"></div>

    <h1 class="headline">
      <span class="line-one">Comedy</span>
      <span class="line-two">Hypnotist</span>
    </h1>

    <svg class="details-panel" viewBox="0 0 800 380" aria-hidden="true">
      <path d="M0 60 C 120 30, 260 20, 420 28 C 560 36, 680 10, 800 0 L800 380 L0 380 Z" fill="var(--paper)"/>
    </svg>

    <div class="act-name">Morlan T</div>
  </main>
</body>
</html>
```